Business Card needed for Drainor, a growing Septic Service company

Drainor, a growing local septic service company in Pennsylvania, needs updated business cards. We'd like the business card to feature our logo and communicate that we provide Septic Pumping, Installations/Repairs, Restroom Rentals, and 24/7 Emergency Service. The business card should be eye-catching, bold, and clean/simple. We have been in business almost 10 years and would like to expand and update our business brand and image.

Target Market(s)

Residential and Commercial, New and Current Homeowners

Industry/Entity Type

Service

Contact Information for Business Card

Contact on the business card should be: Dean Harlow Owner & Operator
Phone: 610-555-0187
Email: service@drainor-example.com
Website: www.drainor-example.com
Address: 812 Millbrook Lane Ashvale OH 45999

Font styles to use
Sans Serif

Colors

Designer to choose colors to be used in the design.

Requirements
Must have
• Feature logo on both side of business card.
Nice to have
• We envision the contact information on one side and our services listed on the other side. Utilize the green from the symbol in our logo as part of the design, overall design color scheme should be white, grey, black.

```html
<!DOCTYPE html>
<html lang="en">
<head>
<meta charset="utf-8">
<title>Drainor – Business Card</title>
<link rel="stylesheet" href="https://fonts.googleapis.com/css2?family=Arimo:wght@400;700&display=swap">
<style>
  :root {
    --charcoal: #22272a;
    --brand-green: #6cc31a;
    --frame-lime: #84ea24;
    --ink: #111111;
    --paper: #fdfdfd;
    --role-tint: #eef7e2;
  }
  * { margin: 0; padding: 0; box-sizing: border-box; }
  html, body { width: 1200px; height: 686px; overflow: hidden; background: var(--paper); }
  body { font-family: "Arimo", Arial, sans-serif; }

  .card {
    position: relative;
    width: 1200px;
    height: 686px;
    background: var(--paper);
    overflow: hidden;
  }
  .band-top {
    position: absolute; left: 0; top: 0;
    width: 100%; height: 229px;
    background: var(--charcoal);
  }
  .band-green {
    position: absolute; left: 0; top: 229px;
    width: 100%; height: 71px;
    background: var(--brand-green);
  }
  .service-photo {
    position: absolute;
    left: 700px; top: 255px;
    width: 500px; height: 290px;
    background: radial-gradient(ellipse at 55% 50%, rgba(170,175,170,0.55) 0%, rgba(200,204,200,0.35) 45%, rgba(255,255,255,0) 72%);
  }
  .frame {
    position: absolute;
    left: 23px; top: 32px;
    width: 1154px; height: 624px;
    border: 4px solid var(--frame-lime);
    pointer-events: none;
  }
  .holder-name {
    position: absolute;
    left: 129px; top: 158px;
    font-size: 66px; font-weight: 700;
    color: #ffffff;
    line-height: 1;
    letter-spacing: 0.5px;
  }
  .holder-role {
    position: absolute;
    left: 129px; top: 236px;
    font-size: 25px; font-weight: 400;
    color: var(--role-tint);
    line-height: 1;
  }
  .contact-list {
    position: absolute;
    left: 124px; top: 305px;
    list-style: none;
  }
  .contact-item {
    display: flex; align-items: center;
    height: 67px;
    font-size: 39px; font-weight: 700;
    color: var(--ink);
    white-space: nowrap;
  }
  .contact-item svg { width: 30px; height: 30px; margin-right: 14px; flex: none; }
  .contact-item.address-line2 { padding-left: 44px; }
  .brand {
    position: absolute;
    left: 826px; top: 517px;
    display: flex; align-items: center;
  }
  .brand-mark {
    width: 48px; height: 48px;
    background: var(--brand-green);
    margin-right: 8px;
  }
  .brand-name {
    font-size: 47px; font-weight: 700;
    color: var(--charcoal);
    line-height: 1;
    letter-spacing: 1px;
  }
  .brand-site {
    position: absolute;
    left: 797px; top: 566px;
    width: 300px;
    text-align: right;
    font-size: 22px; font-weight: 400;
    color: var(--ink);
    white-space: nowrap;
  }
</style>
</head>
<body>
  <div class="card">
    <div class="band-top"></div>
    <div class="band-green"></div>
    <div class="service-photo" role="img" aria-label="Photo of an open septic tank lid with a pumping hose"></div>

    <h1 class="holder-name">Dean Harlow</h1>
    <p class="holder-role">Owner &amp; Operator</p>

    <ul class="contact-list">
      <li class="contact-item">
        <svg viewBox="0 0 24 24" aria-hidden="true"><path fill="#111" d="M6.6 10.8a15.1 15.1 0 0 0 6.6 6.6l2.2-2.2a1 1 0 0 1 1-.25 11.4 11.4 0 0 0 3.6.57 1 1 0 0 1 1 1V20a1 1 0 0 1-1 1A17 17 0 0 1 3 4a1 1 0 0 1 1-1h3.5a1 1 0 0 1 1 1c0 1.25.2 2.45.57 3.57a1 1 0 0 1-.25 1z"/><path fill="none" stroke="#c0392b" stroke-width="1.6" stroke-linecap="round" d="M14.5 3.5a6 6 0 0 1 6 6M14.5 7a2.6 2.6 0 0 1 2.6 2.6"/></svg>
        610-555-0187
      </li>
      <li class="contact-item">
        <svg viewBox="0 0 24 24" aria-hidden="true"><rect x="2" y="5" width="20" height="14" fill="#111"/><path d="M2.5 5.5 12 13l9.5-7.5" fill="none" stroke="#fff" stroke-width="1.6"/></svg>
        service@drainor-example.com
      </li>
      <li class="contact-item">
        <svg viewBox="0 0 24 24" aria-hidden="true"><path fill="#111" d="M12 2a6 6 0 0 0-6 6c0 4.5 6 11 6 11s6-6.5 6-11a6 6 0 0 0-6-6zm0 8.3A2.3 2.3 0 1 1 12 5.7a2.3 2.3 0 0 1 0 4.6z"/><ellipse cx="12" cy="21" rx="5" ry="1.4" fill="#c0392b"/></svg>
        812 Millbrook Lane Ashvale
      </li>
      <li class="contact-item address-line2">OH 45999</li>
    </ul>

    <div class="brand">
      <div class="brand-mark"></div>
      <span class="brand-name">DRAINOR</span>
    </div>
    <p class="brand-site">www.drainor-example.com</p>

    <div class="frame"></div>
  </div>
</body>
</html>
```